Medical group practice

We need a flyer design incorporating the three doctors in the practice, there is a general practitioner, ophthalmologist and an obstetrician & Gynaecologist. see the attached file for the concept. will leave the colour design up to you

Target Market(s)

general public

Industry/Entity Type

Health Care

Colors

Designer to choose colors to be used in the design.

Requirements
Must have
• logos included in attachement

```html
<!DOCTYPE html>
<html lang="en">
<head>
<meta charset="UTF-8">
<title>Verdale Medical – Practice Flyer</title>
<link rel="stylesheet" href="https://fonts.googleapis.com/css2?family=Exo+2:wght@500;600&family=Titillium+Web:wght@400;600&display=swap">
<style>
:root{
  --green:#8dbf3f;
  --green-band:rgba(141,191,63,.92);
  --blue:#4c9cce;
  --heading-blue:#3a8cc6;
  --grey-dark:#8a8a8a;
  --grey-mid:#949494;
  --grey-light:#9e9e9e;
  --ink:#333;
  --stage:#ededed;
  --white:#fff;
}
*{box-sizing:border-box;margin:0;padding:0}
html,body{width:1200px;height:800px;overflow:hidden}
body{background:var(--stage);font-family:"Titillium Web",sans-serif;color:var(--ink);position:relative}
.flyer{position:absolute;top:54px;width:488px;height:692px;background:var(--white);overflow:hidden}
.flyer--front{left:80px}
.flyer--back{left:632px}

/* Front */
.hero-photo{position:absolute;left:0;top:0;width:100%;height:365px;
  background:linear-gradient(100deg,#e9e9ea 0%,#f4f4f4 35%,#cfd6d8 60%,#a9cfd9 80%,#e4eef0 100%)}
.brand-band{position:absolute;left:0;top:31px;width:100%;height:114px;background:var(--green-band);
  display:flex;align-items:center;padding-left:54px;gap:14px}
.brand-mark{width:30px;height:30px;border-radius:50%;background:var(--white)}
.brand-name{font-family:"Exo 2",sans-serif;font-weight:500;font-size:31px;color:var(--white);letter-spacing:.5px}
.tagline{position:absolute;left:0;top:365px;width:100%;height:79px;background:var(--blue);
  display:flex;align-items:center;justify-content:center;
  font-family:"Exo 2",sans-serif;font-weight:500;font-size:30px;color:var(--white)}
.services{position:absolute;left:0;top:444px;width:100%;height:163px;display:flex;padding-top:24px}
.service{flex:1;text-align:center;font-size:12px;line-height:15px}
.service-icon{width:60px;height:54px;margin:0 auto 12px;border-radius:10px;background:var(--green);opacity:.85}
.service-name{font-weight:600;text-transform:uppercase}
.info-bar{position:absolute;left:0;bottom:0;width:100%;height:85px;display:flex;color:var(--white);font-size:12px;line-height:15px}
.info-cell{display:flex;flex-direction:column;justify-content:center;align-items:center;text-align:center}
.info-cell--label{width:167px;background:var(--grey-dark);font-weight:600;text-transform:uppercase}
.info-cell--hours{width:152px;background:var(--grey-mid)}
.info-cell--hours strong{font-weight:600;text-transform:uppercase}
.info-cell--address{flex:1;background:var(--grey-light)}

/* Back */
.back-photo{position:absolute;right:0;top:0;width:190px;height:100%;
  background:linear-gradient(90deg,rgba(255,255,255,0) 0%,rgba(200,220,235,.55) 55%,rgba(150,190,220,.75) 100%);z-index:2;pointer-events:none}
.doctor{position:relative;height:230px}
.doctor:last-child{height:232px}
.doctor-head{height:120px;position:relative;background:var(--white)}
.doctor-icon{position:absolute;left:48px;top:27px;width:72px;height:66px;border-radius:12px;background:var(--green);opacity:.85}
.specialty{position:absolute;left:185px;top:30px;font-family:"Exo 2",sans-serif;font-weight:600;font-size:26px;line-height:28px;color:var(--heading-blue)}
.email{position:absolute;left:185px;bottom:14px;font-size:12px}
.doctor-body{display:flex;height:110px;color:var(--white)}
.doctor:last-child .doctor-body{height:112px}
.doctor-name{width:169px;background:var(--grey-dark);padding:18px 0 0 22px;font-family:"Exo 2",sans-serif;font-weight:500;font-size:15px;line-height:18px;text-transform:uppercase}
.doctor-name .practice{text-transform:none}
.doctor-list{padding:18px 0 0 15px;font-size:11.5px;line-height:15px}
.doctor-list--a{width:153px;background:var(--grey-mid)}
.doctor-list--b{flex:1;background:var(--grey-light);padding-left:11px}
</style>
</head>
<body>

<section class="flyer flyer--front">
  <div class="hero-photo" role="img" aria-label="Photo of a doctor in a white coat holding a stethoscope in a bright clinic"></div>
  <header class="brand-band">
    <span class="brand-mark"></span>
    <span class="brand-name">VERDALE MEDICAL</span>
  </header>
  <div class="tagline">Your Health is Our Priority</div>
  <div class="services">
    <div class="service">
      <div class="service-icon" role="img" aria-label="General practitioner icon"></div>
      <div class="service-name">General<br>Practitioner</div>
      <div>(555) 201 4417,</div>
    </div>
    <div class="service">
      <div class="service-icon" role="img" aria-label="Ophthalmologist icon"></div>
      <div class="service-name">Ophthalmologist</div>
      <div>(555) 201 4532,</div>
    </div>
    <div class="service">
      <div class="service-icon" role="img" aria-label="Obstetrician and gynaecologist icon"></div>
      <div class="service-name">Obstetrician/<br>Gynaecologist</div>
      <div>(555) 201 4680<br>(555) 309 2274</div>
    </div>
  </div>
  <footer class="info-bar">
    <div class="info-cell info-cell--label">Opening Hours</div>
    <div class="info-cell info-cell--hours">
      <strong>Monday-Friday</strong>9am – 6pm<strong>Saturdays</strong>10am – 5pm
    </div>
    <div class="info-cell info-cell--address">
      42 Harbour Lane,<br>Eastport, Westmere<br>Tel : (555) 466 3810 / 3811
    </div>
  </footer>
</section>

<section class="flyer flyer--back">
  <div class="back-photo" role="img" aria-label="Faded photo of a doctor's hands holding a tablet with medical interface graphics"></div>

  <article class="doctor">
    <div class="doctor-head">
      <div class="doctor-icon" role="img" aria-label="General practitioner icon"></div>
      <h2 class="specialty">General Practitioner</h2>
      <div class="email">Email: l.harcourt.clinic@mailbox.com</div>
    </div>
    <div class="doctor-body">
      <div class="doctor-name">Dr. Lionel<br>Harcourt, MD.</div>
      <div class="doctor-list doctor-list--a">General Checks<br>Annual Check ups<br>Wound Care/Dressings<br>Incision &amp; Drainage</div>
      <div class="doctor-list doctor-list--b">Suturing lacerations<br>Pain Injections<br>Glucose checks<br>Foreign Body Removal</div>
    </div>
  </article>

  <article class="doctor">
    <div class="doctor-head">
      <div class="doctor-icon" role="img" aria-label="Ophthalmologist icon"></div>
      <h2 class="specialty">Surgeon<br>Ophthalmologist</h2>
      <div class="email">Email: ines.eyecare@mailbox.com</div>
    </div>
    <div class="doctor-body">
      <div class="doctor-name">Dr. Ines V.<br>Caldera MD.<br><span class="practice">Clearfield Vision<br>Services</span></div>
      <div class="doctor-list doctor-list--a">Eyes disease<br>examination,<br>Surgery of Pterygium,<br>Cataract,</div>
      <div class="doctor-list doctor-list--b">Glaucoma, Emergency:<br>Conjunctivitis,<br>Traumatism, Foreign<br>body and more</div>
    </div>
  </article>

  <article class="doctor">
    <div class="doctor-head">
      <div class="doctor-icon" role="img" aria-label="Obstetrician and gynaecologist icon"></div>
      <h2 class="specialty">Obstetrician &amp;<br>Gynaecologist</h2>
      <div class="email">Email: dr.verloe@mailbox.com</div>
    </div>
    <div class="doctor-body">
      <div class="doctor-name">Dr. Anand Verloe,<br><span class="practice">BMedSci, MBBS, DM<br>(O&amp;G), FACOG</span></div>
      <div class="doctor-list doctor-list--a">Obstetrics:<br>Prenatal Care,<br>Delivery,<br>Postnatal checks,<br>High Risk pregnancy</div>
      <div class="doctor-list doctor-list--b">Gynaecology : Pap smears,<br>Abnormal vaginal bleeding,<br>Fibroids, Colposcopy,<br>Family planning,<br>Infertility, Cancer<br>screening, And More...</div>
    </div>
  </article>
</section>

</body>
</html>
```